Would like to get a new Ticket jacket or caddy design with a modern look for our travel company. Currently we use a one sided design. Photos attached. This ticket jacket will be used to put the domestic tickets for the resort islands and will be handed over to visitors. Free to use Maldives photos from http://lanternfinch.example for ideas.

Project Deadline Extended
Reason: Please give 5 more days for selecting the best design and tweaking the final product

Target Market(s)

Travellers

Industry/Entity Type

Travel

Font styles to use
Sans Serif

Requirements
Must have
• Maldives photos, company addresses(Maldives and London)
Nice to have
• open to ideas
Should not have
• photos in photos or framed photos

```html
<!DOCTYPE html>
<html lang="en">
<head>
<meta charset="utf-8">
<title>Lanternfinch – Ticket Jacket</title>
<link href="https://fonts.googleapis.com/css2?family=Arimo:wght@400;700&display=swap" rel="stylesheet">
<style>
  :root {
    --backdrop: #d9dde3;
    --brand-blue: #1f4e96;
    --panel-text: #ffffff;
    --sky-top: #a9b9c6;
    --sky-mid: #cdd8de;
    --sky-low: #e4eaec;
    --horizon: #2f6f7c;
    --surf: #7fc3c4;
    --lagoon: #4f9ea2;
    --lagoon-mid: #3c8f95;
    --lagoon-deep: #2d7a7f;
  }
  * { margin: 0; padding: 0; box-sizing: border-box; }
  html, body {
    width: 1200px; height: 801px; overflow: hidden;
    background: var(--backdrop);
    font-family: "Arimo", Arial, sans-serif;
  }
  .ticket-jacket {
    position: absolute; left: 100px; top: 134px;
    width: 1000px; height: 532px;
    display: flex;
    box-shadow: 0 10px 30px rgba(0,0,0,0.18);
  }
  .brand-panel {
    width: 205px; height: 100%;
    flex: none;
    background: var(--brand-blue);
    color: var(--panel-text);
    position: relative;
  }
  .brand-name {
    position: absolute; top: 170px; left: 27px;
    font-size: 20px; font-weight: 700; letter-spacing: 0.3px;
    line-height: 24px;
  }
  .brand-subtitle {
    position: absolute; top: 195px; left: 27px;
    font-size: 18px; font-weight: 400; line-height: 22px;
  }
  .office {
    position: absolute; left: 27px;
    font-size: 9.5px; line-height: 13.5px;
    font-style: normal;
  }
  .office p { white-space: nowrap; }
  .office .city { font-weight: 700; }
  .office .gap { height: 13.5px; }
  .office-london { top: 310px; }
  .office-male { top: 430px; }
  .resort-photo {
    flex: 1; height: 100%;
    background: linear-gradient(180deg,
      var(--sky-top) 0%, var(--sky-mid) 18%, var(--sky-low) 32%,
      var(--horizon) 33%, var(--surf) 36%, var(--lagoon) 39%,
      var(--lagoon-mid) 65%, var(--lagoon-deep) 100%);
  }
</style>
</head>
<body>
  <main class="ticket-jacket">
    <section class="brand-panel">
      <h1 class="brand-name">LANTERNFINCH</h1>
      <h2 class="brand-subtitle">Corvel Travel LTD</h2>

      <address class="office office-london">
        <p>Marlow House</p>
        <p>48 Calder Rise</p>
        <p><span class="city">London</span> SW9 2QT</p>
        <div class="gap"></div>
        <p>tel : +44 20 7946 0123</p>
        <p>fax: +44 20 7946 0456</p>
        <p>email: info@lanternfinch.example</p>
      </address>

      <address class="office office-male">
        <p>Ma. Fehimaa Vaadhee</p>
        <p class="city">Male'</p>
        <p>Republic of Maldives</p>
        <div class="gap"></div>
        <p>tel : +960 300 1234</p>
        <p>fax: +960 300 5678</p>
        <p>email: info@lanternfinch.example</p>
      </address>
    </section>

    <div class="resort-photo" role="img"
         aria-label="Photo of a Maldives lagoon under a cloudy sky with surf on the reef, and a guest relaxing on the wooden deck of an overwater villa"></div>
  </main>
</body>
</html>
```